Stonebay Towing Business Card

Towing
Accident towing
Mechanical breakdown
Insurance, salvage and recovery
4wd off road towing
Light & Heavy towing
8347 2516
24 hour business 7 days

Logo can be whole size on front

Industry/Entity Type

Towing/ transport

Contact Information for Business Card

The above

```html
<!DOCTYPE html>
<html lang="en">
<head>
<meta charset="utf-8">
<title>Stonebay Towing Business Card</title>
<link rel="stylesheet" href="https://fonts.googleapis.com/css2?family=Montserrat:wght@600;700;800&display=swap">
<style>
  :root {
    --backdrop: #3a3a3a;
    --card: #141414;
    --card-edge: #232323;
    --red: #d8323d;
    --white: #f4f4f4;
  }
  * { box-sizing: border-box; margin: 0; padding: 0; }
  html, body {
    width: 1200px;
    height: 875px;
    overflow: hidden;
    background: var(--backdrop);
    font-family: "Montserrat", sans-serif;
  }
  .canvas {
    width: 1200px;
    height: 875px;
    display: flex;
    align-items: center;
    justify-content: center;
    gap: 40px;
  }
  .card {
    width: 520px;
    height: 300px;
    border-radius: 18px;
    background: linear-gradient(135deg, var(--card-edge), var(--card) 60%);
    position: relative;
    overflow: hidden;
  }
  .card-front {
    display: flex;
    flex-direction: column;
    align-items: center;
    justify-content: center;
    gap: 22px;
  }
  .brand-name {
    color: var(--red);
    font-weight: 800;
    font-size: 48px;
    letter-spacing: 0.5px;
    line-height: 1;
    text-align: center;
  }
  .tagline {
    color: var(--red);
    font-weight: 700;
    font-size: 19px;
    letter-spacing: 0.3px;
  }
  .card-back {
    display: flex;
    align-items: center;
    padding: 0 34px 0 34px;
  }
  .back-identity {
    width: 205px;
    display: flex;
    flex-direction: column;
    align-items: center;
    gap: 16px;
  }
  .back-identity .brand-name {
    font-size: 26px;
  }
  .phone {
    color: var(--red);
    font-weight: 700;
    font-size: 30px;
    letter-spacing: 0.5px;
  }
  .divider {
    width: 2px;
    height: 180px;
    background: var(--red);
    margin: 0 22px 0 14px;
  }
  .services-title {
    color: var(--white);
    font-weight: 700;
    font-size: 21px;
    margin-bottom: 12px;
  }
  .services-list {
    list-style: none;
  }
  .services-list li {
    color: var(--white);
    font-weight: 600;
    font-size: 13px;
    line-height: 1.95;
    display: flex;
    align-items: center;
    gap: 9px;
  }
  .services-list li::before {
    content: "";
    width: 6px;
    height: 6px;
    border-radius: 50%;
    background: var(--red);
    flex: none;
  }
</style>
</head>
<body>
  <main class="canvas">
    <section class="card card-front" aria-label="Card front">
      <h1 class="brand-name">Stonebay Towing</h1>
      <p class="tagline">24 hour business 7 days</p>
    </section>

    <section class="card card-back" aria-label="Card back">
      <div class="back-identity">
        <p class="brand-name">Stonebay Towing</p>
        <p class="phone">8347 2516</p>
      </div>
      <div class="divider"></div>
      <div class="services">
        <h2 class="services-title">Our Services</h2>
        <ul class="services-list">
          <li>Accident Towing</li>
          <li>Mechanical Breakdown</li>
          <li>Insurance, Salvage &amp; Recovery</li>
          <li>4WD Off-Road Towing</li>
          <li>Light &amp; Heavy Towing</li>
        </ul>
      </div>
    </section>
  </main>
</body>
</html>
```